Plumbing Website

Design a simple 4 page website based on our provided logo and sketches. Winning designer should be willing to upgrade as needed (for additional fee). A design that includes SEO features is a plus.
I would like to see Home, , Services, Recent Jobs (set up for pictures), Contact. I like the water dropplet back ground. Please dont put logo in a box. File attached as exaple only, I am looking for a request service now button in the middle that will have a form fill to be emailed to two different addresses,
I would like to see vibrant colors. Examples of sites I like are www.maplewickplumbingandheat.com look also at www.kfv-fernvalleyplumbing.com - this site is too busy but has good seo features.

```html
<!DOCTYPE html>
<html lang="en">
<head>
<meta charset="utf-8">
<title>Contact – Sierra Crest Plumbing</title>
<link href="https://fonts.googleapis.com/css2?family=Source+Sans+3:wght@300;400;600;700&display=swap" rel="stylesheet">
<style>
  :root {
    --brand-blue: #1e64f0;
    --navy: #0d1f6b;
    --footer-navy: #0a1a5c;
    --accent-yellow: #e9c813;
    --emergency-red: #e3141c;
    --ink: #111111;
    --white: #ffffff;
    --map-tone: #e9e6df;
  }
  * { margin: 0; padding: 0; box-sizing: border-box; }
  html, body { width: 919px; height: 1200px; overflow: hidden; background: var(--white); }
  body { font-family: "Source Sans 3", sans-serif; color: var(--ink); position: relative; }
  .page { position: relative; width: 919px; height: 1200px; }

  .brand { position: absolute; left: 42px; top: 22px; display: flex; align-items: center; gap: 10px; }
  .brand-dot { width: 22px; height: 22px; border-radius: 50%; background: var(--brand-blue); }
  .brand-name { font-size: 28px; font-weight: 700; color: var(--brand-blue); line-height: 1; }

  .emergency-button { position: absolute; left: 420px; top: 11px; width: 80px; height: 80px; }

  .header-contact { position: absolute; right: 42px; top: 12px; text-align: center; color: var(--navy); }
  .header-contact .region { font-size: 17px; font-weight: 600; letter-spacing: -0.3px; }
  .header-contact .phone { font-size: 37px; font-weight: 700; line-height: 1.05; }

  .main-nav { position: absolute; left: 42px; top: 107px; width: 835px; height: 38px; background: var(--brand-blue); }
  .main-nav a { position: absolute; top: 0; height: 38px; line-height: 38px; color: var(--white); text-decoration: none; font-weight: 700; font-size: 17px; text-align: center; }
  .main-nav .nav-home { left: 0; width: 108px; }
  .main-nav .nav-services { left: 124px; width: 120px; }
  .main-nav .divider { position: absolute; left: 244px; top: 4px; width: 2px; height: 30px; background: rgba(255,255,255,0.35); }
  .main-nav .nav-jobs { left: 258px; width: 136px; }
  .main-nav .nav-contact { left: 409px; width: 136px; background: var(--accent-yellow); color: var(--navy); border: 1px solid #b89a00; }

  .section-title { position: absolute; left: 42px; font-size: 36px; font-weight: 400; color: var(--brand-blue); }
  .title-contact { top: 202px; }
  .title-find { top: 514px; }

  .address { position: absolute; left: 42px; top: 261px; font-size: 22px; font-style: normal; }
  .address p { height: 34px; line-height: 34px; }
  .address .company { font-weight: 700; }
  .address .fax { margin-top: 7px; }
  .address a { color: var(--brand-blue); text-decoration: none; border-bottom: 1px solid var(--brand-blue); }

  .map-panel { position: absolute; top: 581px; width: 409px; height: 277px; border: 1px solid #9a9a9a; }
  .map-street { left: 42px; background: linear-gradient(160deg, #ecebe6 0%, #e2dfd6 60%, #efe9b8 100%); }
  .map-view { left: 468px; background: linear-gradient(180deg, #9cb6d4 0%, #8aa06c 38%, #7d7b74 55%, #5f5e5a 100%); }

  .tagline { position: absolute; top: 1010px; width: 919px; text-align: center; font-size: 30px; font-weight: 700; color: var(--navy); }

  .site-footer { position: absolute; left: 0; top: 1057px; width: 919px; height: 99px; background: var(--brand-blue); color: var(--white); }
  .footer-nav { position: absolute; left: 42px; top: 16px; font-size: 16px; font-weight: 300; }
  .footer-nav a { color: var(--white); text-decoration: none; }
  .footer-nav span { margin: 0 10px; }
  .footer-contact { position: absolute; right: 42px; top: 15px; text-align: right; }
  .footer-contact .region { font-size: 17px; font-weight: 400; }
  .footer-contact .phone { font-size: 38px; font-weight: 700; line-height: 1.2; }

  .copyright { position: absolute; left: 0; top: 1156px; width: 919px; height: 44px; line-height: 44px; background: var(--footer-navy); color: #c8cbe0; text-align: center; font-size: 14px; font-weight: 300; }
</style>
</head>
<body>
<div class="page">
  <header>
    <div class="brand"><span class="brand-dot"></span><span class="brand-name">Sierra Crest Plumbing</span></div>
    <svg class="emergency-button" viewBox="0 0 80 80" aria-label="Plumbing emergency button">
      <circle cx="40" cy="40" r="39" fill="var(--emergency-red)"/>
      <circle cx="40" cy="40" r="20" fill="var(--white)"/>
      <text x="40" y="17" text-anchor="middle" font-family="Source Sans 3, sans-serif" font-weight="700" font-size="10" fill="#fff">Plumbing</text>
      <text x="40" y="38" text-anchor="middle" font-family="Source Sans 3, sans-serif" font-weight="700" font-size="8" fill="#111">Press</text>
      <text x="40" y="47" text-anchor="middle" font-family="Source Sans 3, sans-serif" font-weight="700" font-size="8" fill="#111">here</text>
      <text x="40" y="70" text-anchor="middle" font-family="Source Sans 3, sans-serif" font-weight="700" font-size="10" fill="#fff">Emergency</text>
    </svg>
    <div class="header-contact">
      <div class="region">CEDAR HOLLOW / PINE RIDGE</div>
      <div class="phone">951-555-0142</div>
    </div>
    <nav class="main-nav">
      <a class="nav-home" href="#">HOME</a>
      <a class="nav-services" href="#">SERVICES</a>
      <span class="divider"></span>
      <a class="nav-jobs" href="#">RECENT JOBS</a>
      <a class="nav-contact" href="#">CONTACT</a>
    </nav>
  </header>

  <main>
    <h1 class="section-title title-contact">Contact Us</h1>
    <address class="address">
      <p class="company">Sierra Crest Plumbing</p>
      <p>2180 W. Orchard Ave Suite 12</p>
      <p>Cedar Hollow CA 90210</p>
      <p>Phone 951-555-0142</p>
      <p class="fax">Fax 888-555-0199</p>
      <p>Email <a href="#">service@sierracrestplumbing.com</a></p>
    </address>

    <h2 class="section-title title-find">Where To Find Us</h2>
    <div class="map-panel map-street" role="img" aria-label="Street map showing the shop location"></div>
    <div class="map-panel map-view" role="img" aria-label="Street-level view of the road outside the shop"></div>

    <p class="tagline">We are looking forward to hearing from you!</p>
  </main>

  <footer class="site-footer">
    <nav class="footer-nav">
      <a href="#">HOME</a><span>/</span><a href="#">SERVICES</a><span>/</span><a href="#">RECENT JOBS</a><span>/</span><a href="#">CONTACT</a>
    </nav>
    <div class="footer-contact">
      <div class="region">CEDAR HOLLOW / PINE RIDGE</div>
      <div class="phone">951-555-0142</div>
    </div>
  </footer>
  <div class="copyright">Copyright © 2013 Sierra Crest Plumbing</div>
</div>
</body>
</html>
```